Medicinal Cannabis Patient Monitoring App

We have a BASIC design for our app for monitoring patients who received Medicinal Cannabis.
The patient would rate how they're feeling after each dose.

The general flow once user is logged in and set up in the system is:

- User should be able to enter the dosing information for the current day
* Consumption Details:
> Enter Time
> Enter Dosage Taken (Added during onboarding)
> Method take to consume the drug
* Score Details:
> Pain Score (On the scale of 1-10)
> Nausea Score (On the scale of 1-10)
> Sedation Score (On the scale of 1-10)
> Wellbeing Score (On the scale of 1-10)
* Blood Pressure Details:
> Pulse
> Blood Pressure Readings
- User should be able to view the instructions
- User should be able to submit the entered details in the platform

We're looking for a clean, medical and SIMPLE design.

OUR USERS are often ELDERLY, Children and disabled individuals. You must consider this in the design.
So, for example, when designing sliders you should consider a creative way to explain the meaning of the slider if the person cant read the word description.

Designs look the same

```html
<!DOCTYPE html>
<html lang="en">
<head>
<meta charset="utf-8">
<title>Step Four – Readings</title>
<link href="https://fonts.googleapis.com/css2?family=Open+Sans:wght@400;600;700&display=swap" rel="stylesheet">
<style>
  :root {
    --green: #35b672;
    --green-line: #2f9f5c;
    --ink: #3b3f44;
    --muted: #6b7177;
    --border: #dcdfe2;
    --bg: #ffffff;
    --scrim: rgba(0, 0, 0, 0.5);
    --white: #ffffff;
  }
  * { box-sizing: border-box; margin: 0; padding: 0; }
  html, body { width: 675px; height: 1200px; overflow: hidden; }
  body {
    position: relative;
    background: var(--bg);
    font-family: "Open Sans", Arial, sans-serif;
    color: var(--ink);
  }
  .status-bar {
    position: absolute; top: 0; left: 0; width: 675px; height: 36px;
    font-size: 22px; font-weight: 600; color: #000;
  }
  .status-bar .carrier { position: absolute; left: 10px; top: 4px; display: flex; align-items: center; gap: 6px; }
  .status-bar .time { position: absolute; left: 0; right: 0; top: 4px; text-align: center; }
  .status-bar .power { position: absolute; right: 10px; top: 4px; display: flex; align-items: center; gap: 8px; }

  .nav-bar { position: absolute; top: 36px; left: 0; width: 675px; height: 90px; }
  .nav-back {
    position: absolute; left: 12px; top: 24px; display: flex; align-items: center; gap: 6px;
    color: var(--green); font-size: 27px;
  }
  .nav-title { position: absolute; left: 0; right: 0; top: 10px; text-align: center; }
  .nav-title .step { font-size: 18px; letter-spacing: 2px; color: var(--muted); text-transform: uppercase; line-height: 24px; }
  .nav-title .name { font-size: 29px; font-weight: 700; color: var(--ink); line-height: 38px; }
  .nav-help { position: absolute; right: 16px; top: 22px; }

  .progress { position: absolute; top: 126px; left: 0; width: 643px; height: 6px; background: var(--green-line); }

  .question {
    position: absolute; left: 0; right: 0; top: 180px; text-align: center;
    font-size: 25px; font-weight: 600; color: var(--ink);
  }
  .reading-box {
    position: absolute; left: 22px; width: 630px; border: 2px solid var(--border); border-radius: 4px;
    display: flex; align-items: center; justify-content: center; gap: 14px;
  }
  .reading-box.pulse { top: 241px; height: 106px; }
  .reading-box.pressure { top: 495px; height: 103px; }
  .reading-value { color: var(--green); font-size: 27px; font-weight: 700; }
  .divider { position: absolute; left: 0; width: 675px; top: 392px; height: 2px; background: var(--border); }

  .submit {
    position: absolute; left: 18px; top: 1075px; width: 639px; height: 104px; border-radius: 52px;
    background: var(--green); color: var(--white); display: flex; align-items: center; justify-content: center; gap: 16px;
    font-size: 29px; font-weight: 700;
  }

  .scrim { position: absolute; inset: 0; background: var(--scrim); }

  .upload-dialog {
    position: absolute; left: 95px; top: 340px; width: 490px; height: 421px;
    background: var(--white); border-radius: 29px;
    display: flex; flex-direction: column; align-items: center;
  }
  .upload-dialog .spinner { margin-top: 95px; }
  .upload-dialog .message {
    margin-top: 40px; text-align: center; font-size: 25.5px; line-height: 40px; color: var(--ink);
  }
</style>
</head>
<body>
  <header class="status-bar">
    <div class="carrier">
      <svg width="34" height="16" viewBox="0 0 34 16"><rect x="0" y="11" width="5" height="5" rx="1" fill="#000"/><rect x="8" y="8" width="5" height="8" rx="1" fill="#000"/><rect x="16" y="4" width="5" height="12" rx="1" fill="#000"/><rect x="24" y="0" width="5" height="16" rx="1" fill="#000"/></svg>
      <span>Carrier</span>
      <svg width="26" height="20" viewBox="0 0 26 20"><path d="M13 19 L2 7 A16 16 0 0 1 24 7 Z" fill="#000"/></svg>
    </div>
    <div class="time">9:41 AM</div>
    <div class="power">
      <svg width="14" height="22" viewBox="0 0 14 22"><path d="M2 6 L12 16 L7 21 V1 L12 6 L2 16" fill="none" stroke="#000" stroke-width="2"/></svg>
      <span>100%</span>
      <svg width="46" height="22" viewBox="0 0 46 22"><rect x="1" y="1" width="40" height="20" rx="4" fill="none" stroke="#000" stroke-width="2"/><rect x="4" y="4" width="34" height="14" rx="2" fill="#000"/><rect x="42" y="7" width="3" height="8" rx="1" fill="#000"/></svg>
    </div>
  </header>

  <nav class="nav-bar">
    <div class="nav-back">
      <svg width="18" height="28" viewBox="0 0 18 28"><path d="M15 3 L4 14 L15 25" fill="none" stroke="var(--green)" stroke-width="3.5" stroke-linecap="round" stroke-linejoin="round"/></svg>
      <span>Back</span>
    </div>
    <div class="nav-title">
      <div class="step">Step Four</div>
      <div class="name">Readings</div>
    </div>
    <svg class="nav-help" width="44" height="44" viewBox="0 0 44 44"><circle cx="22" cy="22" r="19" fill="none" stroke="var(--green)" stroke-width="3.5"/><path d="M16 17 A6 6 0 1 1 23 23 Q22 24 22 27" fill="none" stroke="var(--green)" stroke-width="3.5" stroke-linecap="round"/><circle cx="22" cy="33" r="2.4" fill="var(--green)"/></svg>
  </nav>
  <div class="progress"></div>

  <main>
    <p class="question">What is your pulse reading?</p>
    <div class="reading-box pulse">
      <span class="reading-value">82 bpm</span>
      <svg width="16" height="10" viewBox="0 0 16 10"><path d="M2 2 L8 8 L14 2" fill="none" stroke="var(--ink)" stroke-width="3" stroke-linecap="round" stroke-linejoin="round"/></svg>
    </div>
    <div class="divider"></div>
    <div class="reading-box pressure"></div>
  </main>

  <div class="submit">
    <svg width="34" height="34" viewBox="0 0 34 34"><path d="M32 2 L2 15 L14 19 L32 2 L19 32 L14 19" fill="var(--white)" stroke="var(--white)" stroke-width="2" stroke-linejoin="round"/></svg>
    <span>Submit</span>
  </div>

  <div class="scrim"></div>

  <div class="upload-dialog" role="dialog" aria-label="Uploading">
    <svg class="spinner" width="96" height="96" viewBox="-48 -48 96 96" aria-hidden="true">
      <circle cx="0" cy="36" r="11" fill="var(--green)"/>
      <circle cx="25.5" cy="25.5" r="9" fill="var(--green)"/>
      <circle cx="36" cy="0" r="8" fill="var(--green)"/>
      <circle cx="25.5" cy="-25.5" r="7" fill="var(--green)"/>
      <circle cx="0" cy="-36" r="6" fill="var(--green)"/>
      <circle cx="-25.5" cy="-25.5" r="5" fill="var(--green)"/>
      <circle cx="-36" cy="0" r="4" fill="var(--green)"/>
    </svg>
    <p class="message">Uploading your readings to the<br>confidential database...</p>
  </div>
</body>
</html>
```